For lease banners for Businesses

I need to turn all of these banners into high quality graphics so I can get them printed on vinyl vertical banners that are 44"W x 88"H. So I need them most likely to be vector artwork, and ready to upload to a custom vinyl print shop.

```html
<!DOCTYPE html>
<html lang="en">
<head>
<meta charset="utf-8">
<title>Crestline Holdings – Now Leasing</title>
<link href="https://fonts.googleapis.com/css2?family=Bebas+Neue&family=Oswald:wght@400;500;600&family=Montserrat:wght@400;800&display=swap" rel="stylesheet">
<style>
  :root {
    --ink: #000000;
    --white: #ffffff;
    --gold: #b77c0b;
    --gold-bright: #c68a12;
    --rule: #7a5a1c;
  }
  * { margin: 0; padding: 0; box-sizing: border-box; }
  html, body { width: 1200px; height: 2400px; overflow: hidden; background: var(--ink); }
  .banner { position: relative; width: 1200px; height: 2400px; background: var(--ink); color: var(--white); font-family: "Montserrat", sans-serif; }

  .brand { position: absolute; left: 0; width: 1200px; display: flex; align-items: center; justify-content: center; gap: 40px; }
  .brand-top { top: 109px; height: 144px; }
  .brand-bottom { top: 2158px; height: 130px; }
  .brand-mark { width: 136px; height: 144px; border: 4px solid var(--gold); flex: none; }
  .brand-bottom .brand-mark { width: 124px; height: 130px; }
  .brand-name { font-family: "Montserrat", sans-serif; font-weight: 800; font-size: 46px; line-height: 58px; letter-spacing: 8px; color: var(--white); white-space: nowrap; }
  .brand-bottom .brand-name { font-size: 42px; line-height: 54px; }

  .photo { position: absolute; border: 1px solid var(--gold); }
  .photo-coffee { left: 0; top: 282px; width: 600px; height: 376px; background: radial-gradient(ellipse at 50% 55%, #e8d6bf 0%, #b07a48 28%, #6b3a1c 60%, #2c140a 100%); }
  .photo-street { left: 600px; top: 282px; width: 600px; height: 376px; background: linear-gradient(110deg, #d9dcd8 0%, #f1efe9 35%, #c8b59e 60%, #9ba3a5 100%); }
  .photo-retail { left: 0; top: 993px; width: 600px; height: 316px; background: linear-gradient(180deg, #5d5547 0%, #cdbb98 40%, #e9dcc2 75%, #d6c6a6 100%); }
  .photo-patio { left: 600px; top: 993px; width: 600px; height: 316px; background: linear-gradient(160deg, #6f7467 0%, #a9a594 40%, #56585a 75%, #3a3a3c 100%); }

  .headline { position: absolute; left: 0; top: 672px; width: 1200px; text-align: center; font-family: "Bebas Neue", sans-serif; font-size: 138px; line-height: 112px; letter-spacing: 2px; font-weight: 400; }
  .accent { color: var(--gold-bright); }
  .headline-rule { position: absolute; left: 242px; top: 920px; width: 604px; height: 2px; background: var(--gold); }
  .tagline { position: absolute; left: 0; top: 923px; width: 1200px; text-align: center; font-size: 36px; font-weight: 400; }

  .sectors { position: absolute; left: 0; top: 1322px; width: 1200px; display: flex; justify-content: center; align-items: center; gap: 34px; font-family: "Oswald", sans-serif; font-weight: 500; font-size: 42px; letter-spacing: 2px; }
  .sector-dot { width: 11px; height: 11px; border-radius: 50%; background: var(--gold); }
  .sectors .wide { margin: 0 20px; }

  .features { position: absolute; left: 109px; top: 1391px; width: 982px; list-style: none; }
  .feature { position: relative; height: 112.5px; border-top: 1px solid var(--rule); }
  .feature-icon { position: absolute; left: 10px; top: 18px; width: 76px; height: 76px; }
  .feature-icon * { fill: none; stroke: var(--gold); stroke-width: 2.6; stroke-linecap: round; stroke-linejoin: round; }
  .feature-title { position: absolute; left: 103px; top: 14px; font-family: "Oswald", sans-serif; font-weight: 500; font-size: 32px; letter-spacing: 2px; }
  .feature-text { position: absolute; left: 103px; top: 60px; font-size: 23px; }

  .cta { position: absolute; left: 0; top: 1971px; width: 1200px; height: 172px; background: var(--gold); color: var(--ink); }
  .cta-phone { position: absolute; left: 110px; top: 36px; width: 100px; height: 100px; }
  .cta-label { position: absolute; left: 242px; top: 0; width: 320px; font-family: "Oswald", sans-serif; font-weight: 500; font-size: 60px; line-height: 172px; letter-spacing: -1px; white-space: nowrap; }
  .cta-divider { position: absolute; left: 600px; top: 22px; width: 2px; height: 128px; background: var(--ink); }
  .cta-contact { position: absolute; left: 643px; top: 6px; font-family: "Oswald", sans-serif; color: var(--ink); white-space: nowrap; }
  .cta-contact p { line-height: 54px; }
  .cta-call { font-size: 38px; font-weight: 400; }
  .cta-number { font-size: 42px; font-weight: 600; }
  .cta-email { font-size: 38px; font-weight: 400; letter-spacing: -0.5px; }
</style>
</head>
<body>
<div class="banner">

  <header class="brand brand-top">
    <div class="brand-mark"></div>
    <div class="brand-name">CRESTLINE<br>HOLDINGS</div>
  </header>

  <div class="photo photo-coffee" role="img" aria-label="Latte with leaf art in a white cup on burlap with coffee beans"></div>
  <div class="photo photo-street" role="img" aria-label="Two women chatting while walking downtown with coffee and shopping bag"></div>

  <h1 class="headline">THIS COULD BE <span class="accent">YOUR</span><br><span class="accent">NEXT</span> LOCATION<span class="accent">.</span></h1>
  <div class="headline-rule"></div>
  <p class="tagline">Build your business where people gather.</p>

  <div class="photo photo-retail" role="img" aria-label="Bright clothing store interior with mannequins and racks"></div>
  <div class="photo photo-patio" role="img" aria-label="Friends sharing pizza at an outdoor patio table"></div>

  <div class="sectors">
    <span>RETAIL</span><span class="sector-dot"></span><span class="wide">RESTAURANT</span><span class="sector-dot"></span><span>OFFICE</span>
  </div>

  <ul class="features">
    <li class="feature">
      <svg class="feature-icon" viewBox="0 0 76 76"><path d="M38 70 C24 50 16 40 16 28 a22 22 0 0 1 44 0 c0 12 -8 22 -22 42z"/><circle cx="38" cy="28" r="9"/></svg>
      <h2 class="feature-title">HIGH VISIBILITY</h2>
      <p class="feature-text">Prime location with strong street exposure.</p>
    </li>
    <li class="feature">
      <svg class="feature-icon" viewBox="0 0 76 76"><circle cx="26" cy="22" r="6"/><circle cx="50" cy="22" r="6"/><path d="M16 40 a10 10 0 0 1 20 0 M40 40 a10 10 0 0 1 20 0"/><circle cx="14" cy="40" r="6"/><circle cx="38" cy="40" r="6"/><circle cx="62" cy="40" r="6"/><path d="M3 60 a11 11 0 0 1 22 0z M27 60 a11 11 0 0 1 22 0z M51 60 a11 11 0 0 1 22 0z"/></svg>
      <h2 class="feature-title">DOWNTOWN TRAFFIC</h2>
      <p class="feature-text">Surrounded by thriving businesses, events and foot traffic.</p>
    </li>
    <li class="feature">
      <svg class="feature-icon" viewBox="0 0 76 76"><rect x="6" y="6" width="64" height="64"/><path d="M6 30 H30 V6 M30 50 H6 M46 6 V30 H70 M46 70 V48 H70 M30 50 V70"/><rect x="12" y="12" width="10" height="10"/></svg>
      <h2 class="feature-title">FLEXIBLE FLOORPLANS</h2>
      <p class="feature-text">Customizable layouts to fit your business needs.</p>
    </li>
    <li class="feature">
      <svg class="feature-icon" viewBox="0 0 76 76"><circle cx="38" cy="20" r="13"/><path d="M31 20 l5 5 l9 -10"/><path d="M4 38 H16 V66 H4 M72 38 H60 V66 H72 M16 44 L30 40 L44 48 L60 44 M16 60 L30 66 L46 56"/></svg>
      <h2 class="feature-title">LOCAL OWNERSHIP</h2>
      <p class="feature-text">Proudly owned and invested in downtown.</p>
    </li>
    <li class="feature">
      <svg class="feature-icon" viewBox="0 0 76 76"><path d="M10 10 l8 -4 l10 10 l-4 8 l-8 -2z M24 24 L62 62 l-6 6 L18 30"/><path d="M66 10 a12 12 0 0 0 -16 14 L14 58 a6 6 0 1 0 6 6 L56 28 a12 12 0 0 0 14 -14 l-8 6 l-6 -6z"/></svg>
      <h2 class="feature-title">BUILD-TO-SUIT OPTIONS</h2>
      <p class="feature-text">Opportunities to create the perfect space.</p>
    </li>
  </ul>

  <section class="cta">
    <svg class="cta-phone" viewBox="0 0 100 100"><circle cx="50" cy="50" r="50" fill="#000"/><path d="M34 27 l8 -3 l7 14 l-6 5 c2 7 7 12 14 15 l5 -6 l14 7 l-3 8 c-3 4 -8 5 -13 3 c-14 -5 -25 -16 -30 -30 c-2 -5 -0 -10 4 -13z" fill="var(--gold)"/></svg>
    <div class="cta-label">NOW LEASING</div>
    <div class="cta-divider"></div>
    <div class="cta-contact">
      <p class="cta-call">CALL OR TEXT</p>
      <p class="cta-number">555-014-2370</p>
      <p class="cta-email">leasing@crestlineholdings.com</p>
    </div>
  </section>

  <footer class="brand brand-bottom">
    <div class="brand-mark"></div>
    <div class="brand-name">CRESTLINE<br>HOLDINGS</div>
  </footer>

</div>
</body>
</html>
```